QTR Newsletter

QTR provides mortgage processing outsource services to Mortgage Lenders in Australia and New Zealand. The company employs approximately 300 staff based in offices in Sydney, Melbourne, Brisbane, Adelaide and Perth in Australia and Auckland, New Zealand.
The company acquired a similar and much larger business in 2012 which is being integrated into the one business.
The objectives of a newsletter are to:
- Support the development of the company culture
- Develp a sense of "one team"
- Provide a communication forum for management and staff
I am seeking design options for the newsletter. We will develop/include specific content which will likley evolve over time.
A copy of the company brand gudelines and logo is attached for reference. Our website is currently going through a redesign. Additional information can be provided on request.

Target Market(s)

The target market for the newsletter is staff. This is a diverse group in terms of locations, age, gender, occupations etc.

Industry/Entity Type

Communication

Requirements
Must have
• Information to be included in the newsletter should include:
- Business results (activity, volumes, performance to budget)
- Client news section (recent developments, client profiling etc)
- New initiatives (update on key projects and new business initiatives, initiatives roadmap)
- Office news (news section for each office including new employees, team profile of the month, report on social events)
- CEO report

```html
<!DOCTYPE html>
<html lang="en">
<head>
<meta charset="utf-8">
<title>QTR Newsletter – February 2013</title>
<link href="https://fonts.googleapis.com/css2?family=Open+Sans:wght@400;600;700&display=swap" rel="stylesheet">
<style>
  :root {
    --brand-blue: #0e4f8c;
    --brand-lime: #a7b300;
    --lime-dark: #8f9a00;
    --lime-light: #cdd64a;
    --ink: #3c3c3c;
    --heading-blue: #1c5c98;
    --rule: #dcdcdc;
    --paper: #ffffff;
    --placeholder: #dedede;
  }
  * { box-sizing: border-box; margin: 0; padding: 0; }
  html, body { width: 1200px; height: 3600px; overflow: hidden; }
  body {
    position: relative;
    background: var(--paper);
    font-family: "Open Sans", Arial, sans-serif;
    color: var(--ink);
  }
  .abs { position: absolute; }

  /* Header */
  .header-band {
    left: 0; top: 0; width: 1200px; height: 600px;
    background: var(--brand-lime);
  }
  .header-photo {
    left: 360px; top: 0; width: 540px; height: 345px;
    background: linear-gradient(160deg, #c9d23a 0%, #b4be14 45%, #98a300 100%);
  }
  .masthead-name-box {
    left: 84px; top: 0; width: 291px; height: 246px;
    background: var(--paper);
    border-radius: 0 0 12px 12px;
    display: flex; align-items: center; justify-content: center;
  }
  .masthead-name {
    font-size: 60px; font-weight: 400; color: var(--brand-blue);
    letter-spacing: 4px; line-height: 1;
  }
  .issue-date {
    left: 864px; top: 0; width: 252px; height: 144px;
    background: var(--brand-blue);
    border-radius: 0 0 14px 14px;
    color: #fff; font-size: 30px; font-weight: 600;
    display: flex; align-items: center; justify-content: center;
    padding-top: 10px;
  }
  .content-panel {
    left: 84px; top: 345px; width: 1032px; height: 2976px;
    background: var(--paper);
    border-radius: 18px;
  }
  .intro-banner {
    left: 102px; top: 375px; width: 996px; height: 225px;
    background: var(--brand-blue);
    border-radius: 14px;
    color: #fff; text-align: center;
    padding-top: 38px;
  }
  .intro-banner .title { font-size: 34px; font-weight: 400; line-height: 1.2; }
  .intro-banner .subtitle { font-size: 26px; line-height: 1.3; }
  .social-row { display: flex; justify-content: center; gap: 21px; margin-top: 22px; }
  .social-dot { width: 54px; height: 54px; }

  /* Accent bars */
  .bar-blue { background: var(--brand-blue); }
  .bar-lime { background: var(--brand-lime); }

  /* Sections */
  .section-heading {
    font-size: 33px; font-weight: 400; color: var(--heading-blue);
    text-transform: uppercase; line-height: 1;
  }
  .body-copy { font-size: 20.5px; line-height: 31.5px; color: var(--ink); }
  .rule { height: 2px; background: var(--rule); }
  .more-arrow { width: 18px; height: 24px; }
  .feature-photo {
    width: 354px; height: 240px;
    border: 4px solid var(--lime-light);
    border-radius: 12px;
    background: linear-gradient(135deg, #f2f2ee 0%, #d9dad4 40%, #b9bcb4 70%, #e8e6dc 100%);
  }

  /* Client news */
  .news-title { font-size: 33px; color: #333; line-height: 1; }
  .news-date { font-size: 23px; color: var(--lime-dark); margin-top: 10px; }
  .news-copy { font-size: 19.5px; line-height: 30px; font-weight: 600; color: #333; }

  /* CEO */
  .ceo-photo {
    left: 150px; top: 2979px; width: 255px; height: 252px;
    background: var(--placeholder);
    border: 9px solid #fff;
    box-shadow: 0 0 0 2px #e2e2e2;
  }

  /* Footer */
  .footer-band {
    left: 0; top: 3150px; width: 1200px; height: 450px;
    background: var(--brand-lime);
  }
  .footer-note {
    left: 0; top: 3432px; width: 1200px; text-align: center;
    color: #fff; font-size: 20px; line-height: 34px;
  }
</style>
</head>
<body>

  <!-- Header -->
  <div class="abs header-band"></div>
  <div class="abs header-photo" role="img" aria-label="Photo of a family home held in cupped hands, tinted lime"></div>
  <div class="abs masthead-name-box">
    <div class="masthead-name">QTR</div>
  </div>
  <div class="abs issue-date">FEBRUARY 2013</div>

  <!-- Footer band sits beneath the panel -->
  <div class="abs footer-band"></div>

  <!-- Content panel -->
  <div class="abs content-panel"></div>

  <div class="abs intro-banner">
    <div class="title">PROVIDES MORTGAGE PROCESSING OUTSOURCE SERVICES</div>
    <div class="subtitle">to Mortgage Lenders in Australia and New Zealand</div>
    <div class="social-row">
      <svg class="social-dot" viewBox="0 0 54 54"><circle cx="27" cy="27" r="24" fill="none" stroke="#fff" stroke-width="4"/></svg>
      <svg class="social-dot" viewBox="0 0 54 54"><circle cx="27" cy="27" r="24" fill="none" stroke="#fff" stroke-width="4"/></svg>
      <svg class="social-dot" viewBox="0 0 54 54"><circle cx="27" cy="27" r="24" fill="none" stroke="#fff" stroke-width="4"/></svg>
    </div>
  </div>

  <!-- Accent bars -->
  <div class="abs bar-blue" style="left:1164px;top:684px;width:36px;height:180px"></div>
  <div class="abs bar-lime" style="left:1164px;top:1005px;width:36px;height:180px"></div>
  <div class="abs bar-blue" style="left:1164px;top:1359px;width:36px;height:180px"></div>
  <div class="abs bar-lime" style="left:1164px;top:1665px;width:36px;height:180px"></div>
  <div class="abs bar-blue" style="left:0;top:1929px;width:36px;height:417px"></div>
  <div class="abs bar-lime" style="left:0;top:2454px;width:36px;height:411px"></div>
  <div class="abs bar-blue" style="left:0;top:3015px;width:150px;height:180px"></div>
  <div class="abs bar-blue" style="left:1116px;top:3009px;width:84px;height:171px"></div>

  <!-- Company culture -->
  <h2 class="abs section-heading" style="left:78px;top:687px">Company Culture</h2>
  <p class="abs body-copy" style="left:78px;top:741px;width:1035px">Lorem Ipsum is simply dummy text of the printing and typesetting industry. Lorem Ipsum has been the industry's standard dummy text ever since the 1500s, when an unknown printer took a galley of type and scrambled it to make a type specimen book. It has survived not only five centuries, but also the leap into electronic typesetting, remaining essentially unchanged.</p>
  <svg class="abs more-arrow" style="left:1086px;top:864px" viewBox="0 0 18 24"><path d="M0 0L18 12L0 24Z" fill="#111"/></svg>
  <div class="abs rule" style="left:78px;top:911px;width:1038px"></div>

  <!-- Business activity -->
  <div class="abs feature-photo" style="left:84px;top:981px" role="img" aria-label="Photo of a mortgage application form with a calculator and pen"></div>
  <h2 class="abs section-heading" style="left:474px;top:969px">Business Activity</h2>
  <p class="abs body-copy" style="left:474px;top:1023px;width:640px">Lorem Ipsum is simply dummy text of the printing and typesetting industry. Lorem Ipsum has been the industry's standard dummy text ever since the 1500s, when an unknown printer took a galley of type and scrambled it to make a type specimen book. It has survived not only five centuries, but also the leap into electronic typesetting, remaining essentially unchanged.</p>
  <svg class="abs more-arrow" style="left:1086px;top:1224px" viewBox="0 0 18 24"><path d="M0 0L18 12L0 24Z" fill="#111"/></svg>
  <div class="abs rule" style="left:78px;top:1269px;width:1038px"></div>

  <!-- Company infrastructure -->
  <h2 class="abs section-heading" style="left:78px;top:1308px">Company Infrastructure</h2>
  <p class="abs body-copy" style="left:78px;top:1362px;width:1035px">Lorem Ipsum is simply dummy text of the printing and typesetting industry. Lorem Ipsum has been the industry's standard dummy text ever since the 1500s, when an unknown printer took a galley of type and scrambled it to make a type specimen book. It has survived not only five centuries, but also the leap into electronic typesetting, remaining essentially unchanged.</p>
  <svg class="abs more-arrow" style="left:1086px;top:1488px" viewBox="0 0 18 24"><path d="M0 0L18 12L0 24Z" fill="#111"/></svg>
  <div class="abs rule" style="left:78px;top:1548px;width:1038px"></div>

  <!-- Business results -->
  <div class="abs feature-photo" style="left:84px;top:1605px" role="img" aria-label="Photo of a mortgage application form with a calculator and charts"></div>
  <h2 class="abs section-heading" style="left:474px;top:1602px">Business Results</h2>
  <p class="abs body-copy" style="left:474px;top:1656px;width:640px">Lorem Ipsum is simply dummy text of the printing and typesetting industry. Lorem Ipsum has been the industry's standard dummy text ever since the 1500s, when an unknown printer took a galley of type and scrambled it to make a type specimen book. It has survived not only five centuries, but also the leap into electronic typesetting, remaining essentially unchanged.</p>
  <svg class="abs more-arrow" style="left:1086px;top:1848px" viewBox="0 0 18 24"><path d="M0 0L18 12L0 24Z" fill="#111"/></svg>
  <div class="abs rule" style="left:78px;top:1893px;width:1038px"></div>

  <!-- Company news 1 -->
  <h2 class="abs section-heading" style="left:78px;top:1929px">Company News</h2>
  <p class="abs body-copy" style="left:78px;top:1980px;width:1035px">Lorem Ipsum is simply dummy text of the printing and typesetting industry. Lorem Ipsum has been the industry's standard dummy text ever since the 1500s.</p>

  <div class="abs" style="left:90px;top:2088px">
    <div class="news-title">Client news1</div>
    <div class="news-date">04.02.2013</div>
  </div>
  <p class="abs news-copy" style="left:330px;top:2085px;width:740px">Lorem Ipsum is simply dummy text of the printing and typesetting industry. Lorem Ipsum has been the industry's standard dummy text ever since the 1500s, when an unknown printer took a galley of type and scrambled it to make a type specimen book</p>
  <svg class="abs more-arrow" style="left:1086px;top:2166px" viewBox="0 0 18 24"><path d="M0 0L18 12L0 24Z" fill="#111"/></svg>
  <div class="abs rule" style="left:78px;top:2220px;width:1038px"></div>

  <div class="abs" style="left:90px;top:2241px">
    <div class="news-title">Client news1</div>
    <div class="news-date">04.02.2013</div>
  </div>
  <p class="abs news-copy" style="left:330px;top:2238px;width:740px">Lorem Ipsum is simply dummy text of the printing and typesetting industry. Lorem Ipsum has been the industry's standard dummy text ever since the 1500s, when an unknown printer took a galley of type and scrambled it to make a type specimen book</p>
  <svg class="abs more-arrow" style="left:1086px;top:2343px" viewBox="0 0 18 24"><path d="M0 0L18 12L0 24Z" fill="#111"/></svg>
  <div class="abs rule" style="left:78px;top:2406px;width:1038px"></div>

  <!-- Company news 2 -->
  <h2 class="abs section-heading" style="left:78px;top:2451px">Company News</h2>
  <p class="abs body-copy" style="left:78px;top:2502px;width:1035px">Lorem Ipsum is simply dummy text of the printing and typesetting industry. Lorem Ipsum has been the industry's standard dummy text ever since the 1500s.</p>

  <div class="abs" style="left:90px;top:2604px">
    <div class="news-title">Client news1</div>
    <div class="news-date">04.02.2013</div>
  </div>
  <p class="abs news-copy" style="left:330px;top:2601px;width:740px">Lorem Ipsum is simply dummy text of the printing and typesetting industry. Lorem Ipsum has been the industry's standard dummy text ever since the 1500s, when an unknown printer took a galley of type and scrambled it to make a type specimen book</p>
  <svg class="abs more-arrow" style="left:1086px;top:2670px" viewBox="0 0 18 24"><path d="M0 0L18 12L0 24Z" fill="#111"/></svg>
  <div class="abs rule" style="left:78px;top:2733px;width:1038px"></div>

  <div class="abs" style="left:90px;top:2760px">
    <div class="news-title">Client news1</div>
    <div class="news-date">04.02.2013</div>
  </div>
  <p class="abs news-copy" style="left:330px;top:2757px;width:740px">Lorem Ipsum is simply dummy text of the printing and typesetting industry. Lorem Ipsum has been the industry's standard dummy text ever since the 1500s, when an unknown printer took a galley of type and scrambled it to make a type specimen book</p>
  <svg class="abs more-arrow" style="left:1086px;top:2850px" viewBox="0 0 18 24"><path d="M0 0L18 12L0 24Z" fill="#111"/></svg>
  <div class="abs rule" style="left:78px;top:2925px;width:1038px"></div>

  <!-- CEO report -->
  <div class="abs ceo-photo" role="img" aria-label="Portrait of the chief executive"></div>
  <h2 class="abs section-heading" style="left:441px;top:2982px">CEO Report</h2>
  <p class="abs body-copy" style="left:441px;top:3039px;width:672px">Lorem Ipsum is simply dummy text of the printing and typesetting industry. Lorem Ipsum has been the industry's standard dummy text ever since the 1500s, when an unknown printer took a galley of type and scrambled it to make a type specimen book</p>
  <svg class="abs more-arrow" style="left:1086px;top:3174px" viewBox="0 0 18 24"><path d="M0 0L18 12L0 24Z" fill="#111"/></svg>

  <!-- Footer -->
  <div class="abs social-row" style="left:0;top:3348px;width:1200px;margin:0">
    <svg class="social-dot" viewBox="0 0 54 54"><circle cx="27" cy="27" r="24" fill="none" stroke="#fff" stroke-width="4"/></svg>
    <svg class="social-dot" viewBox="0 0 54 54"><circle cx="27" cy="27" r="24" fill="none" stroke="#fff" stroke-width="4"/></svg>
    <svg class="social-dot" viewBox="0 0 54 54"><circle cx="27" cy="27" r="24" fill="none" stroke="#fff" stroke-width="4"/></svg>
  </div>
  <p class="abs footer-note">You are receiving this email as a part of your company's program.<br>Copyright © 2012 QTR All rights reserved.</p>

</body>
</html>
```